Webdesign für eine Metallfirma
Zielgruppe
Der Auftraggegeber ist eine Metallfirma, welche sich mit Metallbau, Parktechnik,Preßwerkzeugen,Stadtmöblierung
und neu mit Erneuerbaren Energien beschäftigt.
Zielgruppe sind sowohl private als auch geschäftliche Partner, aber auch Städte und Gemeinden.
Aufgabenstellung
- das Layout benötigen wir als PSD
- nur die Startseite soll gelayoutet werden
- die vorherrschende Farbe orientiert sich am Logo, gewünscht ist eine weitere Farbe, da verlassen wir uns auf Ihren Geschmack (siehe anbei)
- die Inhalte der beiden angegebenen Webseiten sollen zusammengeführt werden (siehe unten)
- bitte lassen Sie die Navigationspunkte in allen Ebenen aufklappen

```html
<!DOCTYPE html>
<html lang="de">
<head>
<meta charset="utf-8">
<title>NoKo Metall- und Anlagenbau – Startseite</title>
<link rel="stylesheet" href="https://fonts.googleapis.com/css2?family=PT+Sans:wght@400;700&family=Poppins:wght@300;400;500&display=swap">
<style>
:root{
  --blue:#3d8bd6;
  --blue-dark:#2f74bd;
  --ink:#3a3a3a;
  --muted:#7a7a7a;
  --line:#e6e6e6;
  --panel:#fafafa;
  --bg:#ffffff;
}
*{box-sizing:border-box;margin:0;padding:0}
html,body{width:1200px;height:1200px;overflow:hidden;background:var(--bg)}
body{position:relative;font-family:"Poppins",sans-serif;color:var(--ink)}
.page{position:absolute;left:439px;top:25px;width:313px;height:1158px;background:#fff;box-shadow:0 1px 4px rgba(0,0,0,.18);overflow:hidden}
.abs{position:absolute}
.head-font{font-family:"PT Sans",sans-serif}
.topbar{right:4px;top:2px;font-size:3px;color:var(--blue);font-style:italic}
.brand{left:9px;top:13px;display:flex;align-items:center;gap:3px}
.brand-mark{width:9px;height:9px;background:var(--blue)}
.brand-name{font-family:"PT Sans",sans-serif;font-weight:700;font-size:3.6px;line-height:1.15;color:var(--blue)}
.mainnav{right:4px;top:20px;display:flex;gap:6px;font-size:2.6px;font-weight:500;color:var(--ink)}
.mainnav .active{color:var(--blue)}
.hero{left:0;top:32px;width:313px;height:130px;background:linear-gradient(100deg,#b8a98a 0%,#8c8f93 40%,#c9c2b4 70%,#a7a09a 100%)}
.catnav{left:0;top:162px;width:313px;height:26px;border-bottom:1px solid var(--line);display:flex;align-items:center;justify-content:space-between;padding:0 15px 0 5px;font-family:"PT Sans",sans-serif;font-size:4.6px;color:#555;letter-spacing:.1px}
.intro{left:0;top:209px;width:313px;text-align:center}
.intro h1{font-family:"PT Sans",sans-serif;font-weight:400;font-size:6.4px;color:#444}
.intro p{font-size:4.7px;line-height:1.45;color:#555;margin-top:4px;font-weight:300}
.about{left:9px;top:263px;width:304px;height:101px;background:var(--panel)}
.about-photo{left:0;top:0;width:140px;height:101px;background:linear-gradient(180deg,#d9dde0 0%,#8a8f96 55%,#4e5460 100%)}
.about-text{left:151px;top:0;width:140px}
.about-text h2{font-family:"PT Sans",sans-serif;font-weight:400;font-size:5px;color:#444;margin-top:-1px}
.about-text p{font-size:3px;line-height:1.5;color:#777;margin-top:6px;font-weight:300}
.btn{display:inline-block;background:var(--blue);color:#fff;font-size:2.6px;padding:3px 7px;margin-top:15px;width:60px;text-align:center}
.ticks{left:19px;top:385px;width:280px;display:flex;justify-content:space-between}
.tick{display:flex;gap:3px;align-items:flex-start;width:80px}
.tick svg{margin-top:4px;flex:none}
.tick b{display:block;font-family:"PT Sans",sans-serif;font-weight:400;font-size:4.6px;color:#555}
.tick span{display:block;font-size:2.9px;line-height:1.45;color:#888;font-weight:300}
.whatwedo{left:0;top:430px;width:313px;text-align:center}
.whatwedo h2{font-family:"PT Sans",sans-serif;font-weight:400;font-size:4.9px;color:#555}
.whatwedo p{font-size:3.1px;line-height:1.5;color:#888;margin-top:4px;font-weight:300}
.grid{left:0;top:474px;width:313px}
.row{position:relative;height:97.6px;display:flex}
.cell{width:156.5px;height:100%}
.cell.text{background:var(--panel);position:relative}
.cell.text .inner{position:absolute;top:26px;width:110px}
.cell h3{font-family:"PT Sans",sans-serif;font-weight:700;font-size:4.9px;color:#444}
.cell p{font-size:3px;line-height:1.5;color:#888;margin-top:5px;font-weight:300}
.cell a{display:block;font-size:3px;color:#444;font-weight:500;text-decoration:none}
.img-metal{background:linear-gradient(135deg,#e4e6e8 0%,#9ea3a8 50%,#3a3d42 100%)}
.img-park{background:linear-gradient(120deg,#2d63b8 0%,#3f78c9 50%,#cfa688 100%)}
.img-press{background:linear-gradient(120deg,#b7b3ad 0%,#e6e4e1 55%,#f3f2f0 100%)}
.img-bench{background:linear-gradient(180deg,#6f8f45 0%,#9bc15c 55%,#b9d77a 100%)}
.img-energy{background:linear-gradient(180deg,#4f8fd6 0%,#a9cbef 45%,#2e4f8c 70%,#6f8e3c 100%)}
.cta{left:0;top:963px;width:313px;height:52px;background:var(--blue);color:#fff}
.cta h2{position:absolute;left:17px;top:14px;font-family:"PT Sans",sans-serif;font-weight:700;font-size:5px}
.cta p{position:absolute;left:17px;top:23px;width:195px;font-size:3px;line-height:1.4;font-weight:300}
.cta .mailbtn{position:absolute;left:228px;top:27px;width:73px;height:14px;border:0.6px solid #fff;font-family:"PT Sans",sans-serif;font-size:5px;display:flex;align-items:center;justify-content:center}
.contacts-title{left:0;top:1034px;width:313px;text-align:center;font-family:"PT Sans",sans-serif;font-weight:700;font-size:5px;line-height:1.5;color:#444}
.contacts{left:27px;top:1066px;width:280px;display:flex}
.contact{font-size:2.4px;line-height:1.5;color:#777;font-weight:300}
.contact h4{font-weight:400;font-size:2.4px;color:#666;margin-bottom:5px}
.contact .who{margin-bottom:5px}
.footer-line{left:0;top:1121px;width:313px;border-top:1px solid var(--line)}
.footer{left:7px;top:1131px;width:300px;font-size:2.3px;color:#888;display:flex;gap:6px;font-weight:300}
.footer2{left:8px;top:1148px;font-size:2.3px;color:#888;display:flex;gap:9px;font-weight:300}
</style>
</head>
<body>
<div class="page">
  <div class="abs topbar">Tel.: +49 (0) 30 555 0140-0 &nbsp; / &nbsp; E-Mail: info@noko-metall.de</div>
  <div class="abs brand">
    <div class="brand-mark"></div>
    <div class="brand-name">NoKo Metall- und<br>Anlagenbau GmbH</div>
  </div>
  <nav class="abs mainnav">
    <span class="active">HOME</span><span>WER WIR SIND</span><span>PRODUKTE</span><span>KARRIERE</span><span>AKTUELLES</span><span>KONTAKT</span>
  </nav>

  <div class="abs hero" role="img" aria-label="Foto: zwei Mitarbeiter in der Werkhalle, einer mit gelbem Schutzhelm, einer mit Tablet"></div>

  <nav class="abs catnav">
    <span>METALLBAU</span><span>PARKTECHNIK</span><span>PRESSWERKZEUGE</span><span>STADTMÖBLIERUNG</span><span>ERNEUERBARE ENERGIEN</span>
  </nav>

  <section class="abs intro">
    <h1>NoKo - Ihr verlässlicher Partner</h1>
    <p>Wir sind im Metallbau, &nbsp;Parktechnik, Presswerkzeuge,<br>Stadtmöblierung und erneuerbare Energien tätig.<br>Lorem ipsum dolor sit amet, consectetuer adipiscing elit.</p>
  </section>

  <section class="abs about">
    <div class="abs about-photo" role="img" aria-label="Foto: Team des Unternehmens im Büro"></div>
    <div class="abs about-text">
      <h2>WER WIR SIND</h2>
      <p>Lorem ipsum dolor sit amet, consectetuer adipiscing elit. Aenean commodo ligula eget dolor. Aenean massa. Cum sociis natoque penatibus et magnis dis parturient montes, nascetur ridiculus mus. Donec quam felis, ultricies nec, pellentesque eu, pretium quis, sem. Nulla consequat massa quis enim. Donec pede justo, fringilla vel, aliquet nec, vulputate eget, arcu. In enim justo, rhoncus ut, imperdiet a, venenatis vitae, justo. Nullam dictum felis eu pede mollis pretium. Integer tincidunt. Cras dapibus.</p>
      <span class="btn">Mehr zum Unternehmen</span>
    </div>
  </section>

  <section class="abs ticks">
    <div class="tick">
      <svg width="12" height="9" viewBox="0 0 12 9"><path d="M1 4.5 L4.2 7.6 L11 1" fill="none" stroke="#3d8bd6" stroke-width="1.6"/></svg>
      <div><b>Lorem Ipsum dolor</b><span>Donec quam felis, ultricies nec, pellentesque eu, pretium quis.</span></div>
    </div>
    <div class="tick">
      <svg width="12" height="9" viewBox="0 0 12 9"><path d="M1 4.5 L4.2 7.6 L11 1" fill="none" stroke="#3d8bd6" stroke-width="1.6"/></svg>
      <div><b>Lorem Ipsum dolor</b><span>Donec quam felis, ultricies nec, pellentesque eu, pretium quis.</span></div>
    </div>
    <div class="tick">
      <svg width="12" height="9" viewBox="0 0 12 9"><path d="M1 4.5 L4.2 7.6 L11 1" fill="none" stroke="#3d8bd6" stroke-width="1.6"/></svg>
      <div><b>Lorem Ipsum dolor</b><span>Donec quam felis, ultricies nec, pellentesque eu, pretium quis.</span></div>
    </div>
  </section>

  <section class="abs whatwedo">
    <h2>WAS WIR TUN</h2>
    <p>Donec quam felis, ultricies nec, pellentesque eu, pretium quis, sem.<br>Nulla consequat massa quis enim. Donec pede justo, fringilla vel,<br>aliquet nec, vulputate eget, arcu.</p>
  </section>

  <section class="abs grid">
    <div class="row">
      <div class="cell img-metal" role="img" aria-label="Foto: gestapelte Aluminiumprofile und Rohre"></div>
      <div class="cell text"><div class="inner" style="left:9px;width:110px">
        <h3>Metallbau</h3>
        <p>Herstellung von Metallbauerzeugnissen auf dem Gebiet der Verkehrsleit-, Absperr-, sowie der Werbetechnik, Anfertigung von Zäunen, Gittern, Toren, Geländern, Treppen u.v.m.</p>
        <a>Mehr erfahren</a>
      </div></div>
    </div>
    <div class="row">
      <div class="cell text"><div class="inner" style="left:31px;width:105px">
        <h3>Parktechnik</h3>
        <p>Lieferung und Aufstellung von Parkscheinautomaten, Gebührenautomaten, Schrankenanlagen und kompletten Parksystemen, Polleranlagen sowie Personensperren (Vereinzelungsanlagen).</p>
        <a>Mehr erfahren</a>
      </div></div>
      <div class="cell img-park" role="img" aria-label="Foto: Hand zieht Parkticket aus einem blauen Automaten"></div>
    </div>
    <div class="row">
      <div class="cell img-press" role="img" aria-label="Foto: Handwerker verpresst Rohrleitung mit Presswerkzeug"></div>
      <div class="cell text"><div class="inner" style="left:14px;width:115px">
        <h3>Presswerkzeuge</h3>
        <p>Cum sociis natoque penatibus et magnis dis parturient montes, nascetur ridiculus mus. Donec quam felis, ultricies nec,</p>
        <a>Mehr erfahren</a>
      </div></div>
    </div>
    <div class="row">
      <div class="cell text"><div class="inner" style="left:31px;width:110px;top:37px">
        <h3>Stadtmöblierung</h3>
        <p>Cum sociis natoque penatibus et magnis dis parturient montes, nascetur ridiculus mus. Donec quam felis, ultricies nec,</p>
        <a>Mehr erfahren</a>
      </div></div>
      <div class="cell img-bench" role="img" aria-label="Foto: Parkbank auf sonniger Wiese"></div>
    </div>
    <div class="row">
      <div class="cell img-energy" role="img" aria-label="Foto: Solarfeld mit Windrädern unter blauem Himmel"></div>
      <div class="cell text"><div class="inner" style="left:17px;width:110px;top:35px">
        <h3>Erneuerbare Energien</h3>
        <p>Cum sociis natoque penatibus et magnis dis parturient montes, nascetur ridiculus mus. Donec quam felis, ultricies nec,</p>
        <a>Mehr erfahren</a>
      </div></div>
    </div>
  </section>

  <section class="abs cta">
    <h2>Sie haben Fragen? Wir beraten Sie gerne. Nehmen Sie Kontakt mit uns auf.</h2>
    <p>Lorem ipsum dolor sit amet, consectetuer adipiscing elit. Aenean commodo ligula eget dolor. Aenean massa. Cum sociis natoque penatibus et magnis dis parturient montes, nascetur ridiculus mus. Donec quam felis.</p>
    <div class="mailbtn">E-Mail schreiben</div>
  </section>

  <div class="abs contacts-title">Unsere Ansprechpartner in den Fachbereichen stehen Ihnen gerne telefonisch<br>oder per E-Mail zur Verfügung</div>

  <section class="abs contacts">
    <div class="contact" style="width:63px">
      <h4>PARKTECHNIK</h4><div class="who">Herr Lindner</div>
      Telefon: +49 (0) 30 555 0140-14<br>E-Mail: lindner@noko-metall.de
    </div>
    <div class="contact" style="width:63px">
      <h4>METALLBAU</h4><div class="who">Herr Brandt</div>
      Telefon: +49 (0) 30 555 0140-13<br>E-Mail: brandt@noko-metall.de
    </div>
    <div class="contact" style="width:81px">
      <h4>SANITÄRTECHNIK &amp; ERNEUERBARE ENERGIEN</h4><div class="who">Herr Vogel</div>
      Telefon: +49 (0) 30 555 0140-18<br>E-Mail: vogel@noko-metall.de
    </div>
    <div class="contact" style="width:60px">
      <h4>GESCHÄFTSLEITUNG</h4>
      Telefon: +49 (0) 30 555 0140-0<br>Telefax: +49 (0) 30 555 0140-30<br>E-Mail: &nbsp;info@noko-metall.de
    </div>
  </section>

  <div class="abs footer-line"></div>
  <footer class="abs footer">
    <span>NoKo Metall- und Anlagenbau GmbH</span>
    <span>Am Werkhof 12 | 09999 Musterstadt</span>
    <span>Tel.: +49 (0) 30 555 0140-0 | Fax: +49 (0) 30 555 0140-30</span>
    <span>E-Mail: info@noko-metall.de</span>
  </footer>
  <div class="abs footer2"><span>Datenschutz</span><span>Impressum</span><span>Copyright NoKo 2023</span></div>
</div>
</body>
</html>
```